New Logo design and Business cards

We are changing our business name and require a new Logo and business card design. Our new name will be "Evergrove Garden Design & Construction" with a focus on enhancing our clients lifestyle through correct landscape design and construction of the designed landscape. We are a full service design to construct business meaning we take care of all aspects of designing and creating your ideal outdoor spaces. To see our current work and get a feel for what we do you can go to www.tallpinegardens.com.au. We do not wish to have a major change to the website only the name/logo should change with all current colours etc being used in the new logo and business card. For our Logo I want the logo to reflect who we now are, and what we do, however I want it to have minimal impact on the website with the aim to only need to change the Logo and not colours or text styles. With the business card I need there to be a strong link between the card and the website with colours and looks being similar. I would love to see an image of one of our projects to be included on the card even as a backdrop. I have included a photo that I think could be used in the background of the business card. I have attached a copy of our current business cards (so you with have all relevant information required on the new cards) though I do want a fresh look with strong links to our website. Please feel free to contact me if you have any questions or ideas.

Construction

Evergrove Garden Design & Construction-Bringing outdoor living home.

```html
<!DOCTYPE html>
<html lang="en">
<head>
<meta charset="utf-8">
<title>Evergrove Garden Design &amp; Construction – Business Cards</title>
<link href="https://fonts.googleapis.com/css2?family=Mulish:wght@400;500;600&display=swap" rel="stylesheet">
<style>
  :root {
    --board: #000000;
    --card: #ffffff;
    --ink: #111111;
    --coral: #f07767;
    --coral-pale: #f5b2a7;
    --rule: #4a4a4a;
  }
  * { margin: 0; padding: 0; box-sizing: border-box; }
  html, body {
    width: 1200px; height: 999px; overflow: hidden;
    background: var(--board);
    font-family: "Mulish", "Avenir Next", sans-serif;
  }
  .board { position: relative; width: 1200px; height: 999px; }

  .card {
    position: absolute; left: 286px; width: 628px; height: 392px;
    background: var(--card); overflow: hidden;
  }
  .card--front { top: 83px; }
  .card--back  { top: 527px; }

  .brand { position: absolute; display: flex; align-items: center; }
  .brand__dot { border-radius: 50%; background: var(--coral); flex: none; }
  .brand__text { display: flex; flex-direction: column; }
  .brand__name {
    color: var(--ink); font-weight: 400; line-height: 1; letter-spacing: 0.01em;
  }
  .brand__sub {
    color: var(--ink); font-weight: 500; letter-spacing: 0.14em; white-space: nowrap;
  }
  .brand__plus { color: var(--coral); }

  /* front */
  .card--front .brand { left: 124px; top: 136px; }
  .card--front .brand__dot { width: 81px; height: 81px; margin-right: 21px; }
  .card--front .brand__name { font-size: 55px; }
  .card--front .brand__sub { font-size: 10.5px; margin-top: 5px; }

  .tagline-chip {
    position: absolute; left: 277px; top: 232px; width: 177px; height: 21px;
    background: var(--coral); color: #fff;
    font-size: 7.5px; font-weight: 600; letter-spacing: 0.16em;
    display: flex; align-items: center; justify-content: center; white-space: nowrap;
  }
  .tagline-accent { color: var(--coral-pale); }

  /* back */
  .card--back .brand { left: 43px; top: 148px; }
  .card--back .brand__dot { width: 57px; height: 57px; margin-right: 14px; }
  .card--back .brand__name { font-size: 37px; }
  .card--back .brand__sub { font-size: 7.3px; margin-top: 4px; }

  .divider {
    position: absolute; left: 345px; top: 72px; width: 1.5px; height: 215px;
    background: var(--rule);
  }
  .contact { position: absolute; left: 380px; top: 78px; color: var(--ink); }
  .contact__name { font-size: 20px; font-weight: 500; letter-spacing: 0.03em; line-height: 1.1; }
  .contact__role {
    font-size: 11.5px; color: var(--coral-pale); letter-spacing: 0.08em; margin-top: 2px;
  }
  .contact__list { list-style: none; margin-top: 20px; }
  .contact__row { display: flex; font-size: 16px; line-height: 24.6px; }
  .contact__label { width: 35px; color: var(--coral-pale); }
  .contact__meta { margin-top: 23px; font-size: 9.3px; line-height: 17px; letter-spacing: 0.02em; }
  .contact__sep { color: var(--coral-pale); margin: 0 4px; }

  .footer-band {
    position: absolute; left: 0; bottom: 0; width: 100%; height: 31px;
    background: var(--coral); color: #fff;
    font-size: 8.3px; font-weight: 600; letter-spacing: 0.2em;
    display: flex; align-items: center; justify-content: flex-end; padding-right: 80px;
  }

  /* board signature lockup */
  .board-brand { position: absolute; left: 43px; top: 921px; display: flex; align-items: center; }
  .board-brand .brand__dot { width: 44px; height: 44px; margin-right: 11px; }
  .board-brand .brand__name { color: #fff; font-size: 29px; }
  .board-brand .brand__sub { color: #fff; font-size: 5.6px; margin-top: 3px; }
</style>
</head>
<body>
<main class="board">

  <section class="card card--front" aria-label="Business card front">
    <div class="brand">
      <span class="brand__dot"></span>
      <div class="brand__text">
        <span class="brand__name">EVERGROVE</span>
        <span class="brand__sub">GARDEN DESIGN <span class="brand__plus">+</span> CONSTRUCTION</span>
      </div>
    </div>
    <div class="tagline-chip">BRINGING <span class="tagline-accent">&nbsp;OUTDOOR&nbsp;</span> LIVING HOME</div>
  </section>

  <section class="card card--back" aria-label="Business card back">
    <div class="brand">
      <span class="brand__dot"></span>
      <div class="brand__text">
        <span class="brand__name">EVERGROVE</span>
        <span class="brand__sub">GARDEN DESIGN <span class="brand__plus">+</span> CONSTRUCTION</span>
      </div>
    </div>

    <div class="divider"></div>

    <div class="contact">
      <p class="contact__name">DANA WHITLOCK</p>
      <p class="contact__role">DIRECTOR</p>
      <ul class="contact__list">
        <li class="contact__row"><span class="contact__label">m.</span>0400 218 947</li>
        <li class="contact__row"><span class="contact__label">f.</span>07 3000 5126</li>
        <li class="contact__row"><span class="contact__label">e.</span>dana@evergrovegdc.com.au</li>
        <li class="contact__row"><span class="contact__label">w.</span>evergrovegdc.com.au</li>
      </ul>
      <div class="contact__meta">
        <p>ABN 51824 390 117<span class="contact__sep">|</span>ACN 824 390 117</p>
        <p>MBN 48302<span class="contact__sep">|</span>LQN 742<span class="contact__sep">|</span>AILDM 586</p>
      </div>
    </div>

    <div class="footer-band">BRINGING <span class="tagline-accent">&nbsp;OUTDOOR&nbsp;</span> LIVING HOME</div>
  </section>

  <div class="board-brand">
    <span class="brand__dot"></span>
    <div class="brand__text">
      <span class="brand__name">EVERGROVE</span>
      <span class="brand__sub">GARDEN DESIGN <span class="brand__plus">+</span> CONSTRUCTION</span>
    </div>
  </div>

</main>
</body>
</html>
```